Business Card Design Project

Want a modern business card.
Concern is that our email address is long and thus poses a design challenge.
Items like the company name can be omitted from text as it will be available via the logo.

Example:
Gerald Tunstall
President / CEO
Cell 555.304.1182
Office 555.617.2093
geraldt@korvantsolutionsgroup.example
www.korvantsolutionsgroup.example

Target Market(s)

Technical and executive level members of Information Technology companies in the Healthcare industry.

Industry/Entity Type

Business

Colors

Designer to choose colors to be used in the design.

Requirements
Nice to have
• Raised logo, but I am open.

```html
<!DOCTYPE html>
<html lang="en">
<head>
<meta charset="UTF-8">
<title>Korvant Solutions Group – Business Card</title>
<link href="https://fonts.googleapis.com/css2?family=Open+Sans:wght@400;600;700&display=swap" rel="stylesheet">
<style>
  :root {
    --backdrop: #c9c9c9;
    --navy: #1c3a82;
    --blue-deep: #163f8c;
    --blue-mid: #3f6fc0;
    --blue-light: #8fb0e6;
    --red: #d41f2a;
    --white: #ffffff;
    --card-shadow: rgba(0, 0, 0, 0.28);
  }
  * { margin: 0; padding: 0; box-sizing: border-box; }
  html, body {
    width: 1200px;
    height: 900px;
    overflow: hidden;
    background: var(--backdrop);
    font-family: "Open Sans", Arial, sans-serif;
  }
  .canvas {
    position: relative;
    width: 1200px;
    height: 900px;
  }
  .card {
    position: absolute;
    top: 295px;
    width: 540px;
    height: 310px;
    border-radius: 26px;
    overflow: hidden;
    box-shadow: 0 14px 30px var(--card-shadow);
  }
  .card-front { left: 40px; }
  .card-back { left: 620px; background: var(--white); }

  /* Front */
  .front-pattern {
    position: absolute;
    inset: 0;
    background:
      radial-gradient(ellipse at 85% 70%, rgba(160, 190, 240, 0.55), transparent 60%),
      linear-gradient(110deg, var(--blue-deep) 0%, var(--blue-mid) 55%, var(--blue-light) 100%);
  }
  .front-logo {
    position: absolute;
    left: 0;
    right: 0;
    top: 122px;
    text-align: center;
    color: var(--white);
    font-weight: 700;
    font-size: 30px;
    letter-spacing: 1px;
    line-height: 1.15;
  }

  /* Back */
  .back-pattern {
    position: absolute;
    top: 0;
    right: 0;
    width: 62%;
    height: 100%;
    background: linear-gradient(100deg, rgba(255,255,255,0) 0%, rgba(143,176,230,0.35) 45%, rgba(63,111,192,0.75) 80%, var(--blue-mid) 100%);
  }
  .back-logo {
    position: absolute;
    left: 34px;
    top: 36px;
    color: var(--navy);
    font-weight: 700;
    font-size: 26px;
    letter-spacing: 0.5px;
    line-height: 1.15;
  }
  .person {
    position: absolute;
    left: 34px;
    top: 150px;
  }
  .person-name {
    color: var(--red);
    font-weight: 700;
    font-size: 20px;
    line-height: 1.2;
  }
  .person-title {
    color: var(--navy);
    font-weight: 600;
    font-size: 13px;
    margin-top: 2px;
  }
  .contact-list {
    position: absolute;
    left: 34px;
    top: 222px;
    list-style: none;
  }
  .contact-item {
    display: flex;
    align-items: center;
    gap: 6px;
    color: var(--navy);
    font-weight: 600;
    font-size: 14px;
    line-height: 19px;
  }
  .contact-icon { width: 13px; height: 13px; fill: var(--red); flex: none; }
</style>
</head>
<body>
<main class="canvas">
  <section class="card card-front">
    <div class="front-pattern" role="img" aria-label="Blue background with a sweeping pattern of large light-blue dots"></div>
    <div class="front-logo">KORVANT<br>SOLUTIONS GROUP</div>
  </section>

  <section class="card card-back">
    <div class="back-pattern" role="img" aria-label="Blue halftone dot pattern fading in from the right edge"></div>
    <div class="back-logo">KORVANT<br>SOLUTIONS GROUP</div>

    <div class="person">
      <div class="person-name">Gerald Tunstall</div>
      <div class="person-title">President / CEO</div>
    </div>

    <ul class="contact-list">
      <li class="contact-item">
        <svg class="contact-icon" viewBox="0 0 16 16" aria-hidden="true"><rect x="3" y="0" width="10" height="16" rx="2"/><rect x="5" y="2" width="6" height="8" fill="#fff"/><circle cx="8" cy="13" r="1.2" fill="#fff"/></svg>
        555.304.1182
      </li>
      <li class="contact-item">
        <svg class="contact-icon" viewBox="0 0 16 16" aria-hidden="true"><path d="M3.5 1 L6 4.5 L4.6 6.2 C5.6 8.3 7.7 10.4 9.8 11.4 L11.5 10 L15 12.5 L13.2 15 C7 14.5 1.5 9 1 2.8 Z"/></svg>
        555.617.2093
      </li>
      <li class="contact-item">
        <svg class="contact-icon" viewBox="0 0 16 16" aria-hidden="true"><rect x="0" y="3" width="16" height="11" rx="1.5"/><path d="M1 4 L8 9.5 L15 4" fill="none" stroke="#fff" stroke-width="1.5"/></svg>
        geraldt@korvantsolutionsgroup.example
      </li>
      <li class="contact-item">
        <svg class="contact-icon" viewBox="0 0 16 16" aria-hidden="true"><circle cx="8" cy="8" r="7.5"/><g fill="none" stroke="#fff" stroke-width="1"><ellipse cx="8" cy="8" rx="3" ry="7"/><line x1="1" y1="8" x2="15" y2="8"/><line x1="2" y1="4.5" x2="14" y2="4.5"/><line x1="2" y1="11.5" x2="14" y2="11.5"/></g></svg>
        www.korvantsolutionsgroup.example
      </li>
    </ul>
  </section>
</main>
</body>
</html>
```